TEK Logistics - Banner 2.5' x 8' for 20+ locations

Need a banner designed that will pop. This banner will be displayed at over 20 of our transportation facilities. Goal is for the banner to grab the attention of employees, contractors and clients and help reinforce our mission and core values. Designed needs to include TEK Logo, our core values and mission statement. Red and Black are the main company colors and we need to stay within that theme and color pallet. Attached is a previous version that was too basic and boring. Willing to consider a design that excludes the mission statement.

Gathering more feedback

```html
<!DOCTYPE html>
<html lang="en">
<head>
<meta charset="utf-8">
<title>TEK Logistics – Core Values Banner</title>
<link rel="stylesheet" href="https://fonts.googleapis.com/css2?family=Barlow+Semi+Condensed:wght@600;700&display=swap">
<style>
  :root {
    --brand-red: #d2231a;
    --brand-black: #1b1b1b;
    --paper: #ffffff;
    --backdrop: #e9eaec;
    --ink-light: #ffffff;
  }
  * { box-sizing: border-box; margin: 0; padding: 0; }
  html, body {
    width: 1200px;
    height: 612px;
    overflow: hidden;
    background: var(--backdrop);
    font-family: "Barlow Semi Condensed", "Arial Narrow", sans-serif;
  }
  .banner {
    position: absolute;
    left: 20px;
    top: 125px;
    width: 1160px;
    height: 362px;
    background: var(--paper);
    box-shadow: 0 4px 18px rgba(0,0,0,0.12);
    overflow: hidden;
  }
  .brand {
    position: absolute;
    left: 38px;
    top: 0;
    height: 258px;
    width: 270px;
    display: flex;
    align-items: center;
    gap: 12px;
  }
  .brand-dot {
    width: 22px;
    height: 22px;
    border-radius: 50%;
    background: var(--brand-red);
    flex: none;
  }
  .brand-name {
    font-weight: 700;
    font-size: 44px;
    line-height: 1;
    color: var(--brand-red);
    letter-spacing: 0.5px;
    white-space: nowrap;
  }
  .values {
    position: absolute;
    top: 28px;
    display: flex;
    flex-direction: column;
    gap: 16px;
    list-style: none;
  }
  .values--primary { left: 330px; width: 320px; }
  .values--secondary { left: 700px; width: 330px; }
  .value {
    display: flex;
    align-items: flex-start;
    gap: 14px;
    font-weight: 700;
    font-size: 25px;
    line-height: 1.1;
    color: var(--brand-black);
  }
  .value-tick {
    flex: none;
    width: 20px;
    height: 20px;
    margin-top: 4px;
  }
  .divider {
    position: absolute;
    left: 0;
    right: 0;
    top: 258px;
    height: 5px;
    background: var(--brand-black);
  }
  .mission {
    position: absolute;
    left: 0;
    right: 0;
    top: 263px;
    bottom: 0;
    background: var(--brand-red);
    display: flex;
    align-items: center;
    justify-content: center;
    padding: 0 60px;
  }
  .mission-text {
    color: var(--ink-light);
    font-weight: 700;
    font-size: 25px;
    line-height: 1.2;
    text-align: center;
  }
</style>
</head>
<body>
  <svg width="0" height="0" style="position:absolute" aria-hidden="true">
    <symbol id="tick" viewBox="0 0 20 20">
      <circle cx="10" cy="10" r="8.5" fill="none" stroke="#d2231a" stroke-width="2.2"/>
      <path d="M6 10.3 L8.9 13 L14 7.2" fill="none" stroke="#d2231a" stroke-width="2.2" stroke-linecap="round" stroke-linejoin="round"/>
    </symbol>
  </svg>

  <section class="banner">
    <div class="brand">
      <span class="brand-dot"></span>
      <span class="brand-name">TEK Logistics</span>
    </div>

    <ul class="values values--primary">
      <li class="value"><svg class="value-tick"><use href="#tick"/></svg><span>Do the right things for the right reasons</span></li>
      <li class="value"><svg class="value-tick"><use href="#tick"/></svg><span>Pursue growth and development</span></li>
      <li class="value"><svg class="value-tick"><use href="#tick"/></svg><span>Build a positive team atmosphere</span></li>
    </ul>

    <ul class="values values--secondary">
      <li class="value"><svg class="value-tick"><use href="#tick"/></svg><span>Deliver WOW through service</span></li>
      <li class="value"><svg class="value-tick"><use href="#tick"/></svg><span>Do everything Safely</span></li>
      <li class="value"><svg class="value-tick"><use href="#tick"/></svg><span>Have Fun</span></li>
    </ul>

    <div class="divider"></div>

    <div class="mission">
      <p class="mission-text">Provide the best customer experience while creating an environment of growth and<br>opportunity for our customers, employees, and service providers.</p>
    </div>
  </section>
</body>
</html>
```